Termite Mailer September 2021

We need a clean modern looking flyer advertising termites via the mail.

Size should be 9"x6"

Our tagline is "The Smarter Approach to Pest Control"

Something along the stylistic design of these:

https://pics.hollowmarsh.example/Qa83LkTzWp

https://pics.hollowmarsh.example/Rn47VbXcMd

https://pics.hollowmarsh.example/Hj29PsYeUf

https://www.flintquillprint.example/wp-content/uploads/designs/img/Pest-Prevention-Postcard-PST-1003.jpg

Should include some of this verbiage:

HAVE YOU SCHEDULED YOUR ANNUAL TERMITE INSPECTION? - MAKE IT IN RED

DON'T WAIT. PROTECT YOUR HOME TODAY!

ABSOLUTELY FREE INSPECTION. NO OBLIGATION.

TERMITES CAN CAUSE SEVERE DAMAGE TO YOUR HOME.

BRINDLEVALE LOGO

THE SMARTER APPROACH TO PEST CONTROL.

PROTECT YOUR MOST VALUABLE ASSET.

10% DISCOUNT ON ANY SERVICE GUARANTEED IF YOU CALL TODAY.

INCLUDE A PICTURE OF A TERMITE AS WELL SOMEWHERE AND WOOD DAMAGE.

Target Market(s)

Homeowners in Southern California USA

Industry/Entity Type

Pest Control/Extermination

Font styles to use
Other font styles liked:
• Chaparral Pro Italic, Brava Slab

Requirements
Must have
• Clean design, picture of house, picture of Termite, 10% off coupon and call to action on the back
Should not have
• Bad looking houses, colors that don't match our logo

```html
<!DOCTYPE html>
<html lang="en">
<head>
<meta charset="utf-8">
<title>Termite Inspection Mailer</title>
<link rel="stylesheet" href="https://fonts.googleapis.com/css2?family=Rubik:wght@800;900&family=Montserrat:wght@500;600&display=swap">
<style>
  :root {
    --red: #ec1c24;
    --blue: #0071bc;
    --green: #7ac943;
    --white: #ffffff;
    --photo-sky: #bcd6e6;
    --photo-leaf: #5d7d3f;
    --photo-house: #8a8378;
  }
  * { margin: 0; padding: 0; box-sizing: border-box; }
  html, body { width: 1200px; height: 1200px; overflow: hidden; background: var(--white); }
  .mailer {
    position: absolute; left: 192px; top: 312px;
    width: 824px; height: 582px;
    background: var(--white);
    font-family: "Montserrat", sans-serif;
  }
  .mailer-art { position: absolute; inset: 0; }
  .headline-question {
    position: absolute; left: 336px; top: 30px;
    font-family: "Rubik", sans-serif; font-weight: 900;
    font-size: 24.5px; line-height: 31px; letter-spacing: 2px;
    color: var(--white);
  }
  .headline-main {
    position: absolute; left: 380px; top: 150px;
    font-family: "Rubik", sans-serif; font-weight: 900;
    font-size: 60px; line-height: 1; letter-spacing: 3px;
    color: var(--blue);
  }
  .headline-sub {
    position: absolute; left: 381px; top: 202px;
    font-family: "Rubik", sans-serif; font-weight: 900;
    font-size: 24.5px; line-height: 1.2; letter-spacing: 1.6px;
    color: var(--green);
  }
  .headline-rule {
    position: absolute; left: 380px; top: 242px;
    width: 408px; height: 2px; background: var(--green);
  }
  .selling-points {
    position: absolute; left: 380px; top: 253px;
    font-size: 13.2px; line-height: 19px; font-weight: 500;
    letter-spacing: 0.5px; color: var(--green);
  }
  .offer-discount {
    position: absolute; left: 406px; top: 343px;
    color: var(--white); font-family: "Rubik", sans-serif; font-weight: 900;
  }
  .offer-discount .label { display: block; font-size: 28px; letter-spacing: 1.5px; line-height: 1; }
  .offer-discount .amount { display: block; font-size: 80px; line-height: 0.9; letter-spacing: -1px; margin-left: -2px; }
  .offer-cta {
    position: absolute; left: 620px; top: 346px;
    color: var(--white);
  }
  .offer-cta .label {
    display: block; font-family: "Rubik", sans-serif; font-weight: 900;
    font-size: 22px; letter-spacing: 1.2px; line-height: 1; margin-bottom: 6px;
  }
  .offer-cta p { font-size: 13.2px; line-height: 17.5px; font-weight: 500; letter-spacing: 0.5px; }
  .brand {
    position: absolute; left: 380px; top: 487px;
    display: flex; align-items: center; gap: 6px;
  }
  .brand-mark { width: 30px; height: 30px; border-radius: 50%; background: var(--blue); }
  .brand-name { font-family: "Montserrat", sans-serif; font-weight: 600; font-size: 16px; color: var(--blue); letter-spacing: 0.2px; }
  .brand-divider {
    position: absolute; left: 551px; top: 480px;
    width: 2px; height: 64px; background: var(--green);
  }
  .brand-tagline {
    position: absolute; left: 562px; top: 496px;
    font-size: 9.6px; line-height: 14.5px; font-weight: 600;
    letter-spacing: 0.4px; color: var(--green);
  }
</style>
</head>
<body>
<main class="mailer">
  <svg class="mailer-art" width="824" height="582" viewBox="0 0 824 582">
    <defs>
      <linearGradient id="house-photo-tone" x1="0" y1="0" x2="0.4" y2="1">
        <stop offset="0" stop-color="var(--photo-sky)"/>
        <stop offset="0.35" stop-color="var(--photo-leaf)"/>
        <stop offset="0.65" stop-color="var(--photo-house)"/>
        <stop offset="1" stop-color="#e8e8e4"/>
      </linearGradient>
      <filter id="coupon-shadow" x="-5%" y="-5%" width="110%" height="120%">
        <feDropShadow dx="0" dy="4" stdDeviation="3" flood-color="#000" flood-opacity="0.25"/>
      </filter>
    </defs>
    <rect class="question-band" x="140" y="0" width="684" height="124" fill="var(--red)"/>
    <path class="house-photo" role="img" aria-label="Photo of a shingled house with brick chimney and white front porch among trees"
          d="M0 0 H152 C300 60 380 200 355 330 C335 450 240 550 146 582 H0 Z" fill="url(#house-photo-tone)"/>
    <g class="coupon" filter="url(#coupon-shadow)">
      <rect x="380" y="307" width="444" height="163" fill="var(--green)"/>
      <path d="M614 307 H824 V470 H614 C600 440 598 400 598 388 C598 370 602 340 614 307 Z" fill="var(--blue)"/>
    </g>
    <g class="no-termite-badge">
      <circle cx="264" cy="475" r="94" fill="var(--white)"/>
      <circle cx="264" cy="475" r="47" fill="#555555" role="img" aria-label="Termite illustration"/>
      <circle cx="264" cy="475" r="62" fill="none" stroke="var(--red)" stroke-width="12"/>
      <line x1="308" y1="431" x2="220" y2="519" stroke="var(--red)" stroke-width="11"/>
    </g>
  </svg>

  <h2 class="headline-question">HAVE YOU SCHEDULED YOUR<br>ANNUAL TERMITE INSPECTION?</h2>
  <h1 class="headline-main">DON’T WAIT.</h1>
  <p class="headline-sub">PROTECT YOUR HOME TODAY!</p>
  <div class="headline-rule"></div>
  <p class="selling-points">ABSOLUTELY FREE INSPECTION. NO OBLIGATION.<br>TERMITES CAN CAUSE SEVERE DAMAGE TO YOUR HOME.</p>

  <div class="offer-discount">
    <span class="label">DISCOUNT</span>
    <span class="amount">10%</span>
  </div>
  <div class="offer-cta">
    <span class="label">CALL TODAY</span>
    <p>10% OFF ANY SERVICE<br>GUARANTEED WHEN<br>YOU CALL TODAY.</p>
  </div>

  <div class="brand">
    <span class="brand-mark"></span>
    <span class="brand-name">BRINDLEVALE</span>
  </div>
  <div class="brand-divider"></div>
  <p class="brand-tagline">THE SMARTER APPROACH TO PEST CONTROL.<br>PROTECT YOUR MOST VALUABLE ASSET.</p>
</main>
</body>
</html>
```